Vital Spark Electrical in need of a business card design

We need a new business card designed for our electrical business. We have a logo already which I will attach below.
Would like the business card to be..
-BLACK background preferably, possibly white back ground behind logo if colours clash.
-White & Blue (logo blue) text
Something that makes the logo pop, & a modern look. Possibly minimal clean format.

REQUIRE:
-Logo on front & back

TEXT TO INCLUDE (ON ONE SIDE):

Tom Harlow
Director/Electrician
M: 0417 365 208
E:info@vitalsparkelectrical-example.com.au
W:www.vitalsparkelectrical-example.com.au
R.E.C 57318

Custom/New Homes
Renovations
Commercial Office/Shop Fit-outs
Communications & Security Cameras
Electric Vehicle Chargers
Airconditioning
Updates

Requirements
Nice to have
• Possibly even lighten the grey shades for the words 'Vital' & 'Spark' to be more easily read on a black background.

```html
<!DOCTYPE html>
<html lang="en">
<head>
<meta charset="utf-8">
<title>Vital Spark Electrical – Business Card</title>
<link rel="stylesheet" href="https://fonts.googleapis.com/css2?family=Didact+Gothic&family=Roboto:wght@400;500&display=swap">
<style>
  :root {
    --backdrop: #c6d0d2;
    --card-black: #151515;
    --card-black-soft: #262626;
    --card-white: #ffffff;
    --brand-blue: #33d6f5;
    --brand-navy: #263445;
    --brand-slate: #3f5566;
    --ink-dark: #1b1b1b;
    --text-light: #ffffff;
  }
  * { box-sizing: border-box; margin: 0; padding: 0; }
  html, body {
    width: 1200px;
    height: 1200px;
    overflow: hidden;
    background: var(--backdrop);
  }
  .card {
    position: absolute;
    left: 257px;
    width: 686px;
    height: 390px;
    border-radius: 18px;
    overflow: hidden;
    background: var(--card-white);
  }
  .card--front { top: 173px; }
  .card--back { top: 633px; }

  /* Front */
  .front-panel {
    position: absolute;
    inset: 0 0 78px 0;
    background: radial-gradient(ellipse at 60% 40%, var(--card-black-soft), var(--card-black) 75%);
  }
  .service-list {
    position: absolute;
    left: 209px;
    top: 112px;
    list-style: none;
    font-family: "Didact Gothic", sans-serif;
    font-size: 22px;
    line-height: 24.5px;
    letter-spacing: 0.6px;
    color: var(--text-light);
  }
  .service-list li {
    display: flex;
    align-items: center;
  }
  .service-list li::before {
    content: "";
    width: 17px;
    height: 17px;
    border-radius: 50%;
    background: var(--brand-blue);
    margin-right: 8px;
    flex: none;
  }
  .front-brand {
    position: absolute;
    right: 46px;
    bottom: 22px;
    display: flex;
    align-items: center;
    gap: 10px;
  }

  /* Shared brand name */
  .brand-mark {
    width: 18px;
    height: 18px;
    background: var(--brand-blue);
    flex: none;
  }
  .brand-name {
    font-family: "Roboto", sans-serif;
    font-weight: 500;
    color: var(--brand-slate);
    white-space: nowrap;
  }
  .front-brand .brand-name { font-size: 24px; }

  /* Back */
  .back-brand {
    position: absolute;
    left: 46px;
    top: 58px;
    display: flex;
    align-items: center;
    gap: 16px;
  }
  .back-brand .brand-mark { width: 30px; height: 30px; }
  .back-brand .brand-name { font-size: 38px; }

  .name-plate {
    position: absolute;
    left: 0;
    top: 188px;
    width: 241px;
    height: 90px;
    background: var(--brand-navy);
    color: var(--text-light);
    font-family: "Didact Gothic", sans-serif;
    text-align: center;
    padding-top: 16px;
  }
  .name-plate .person-name {
    font-size: 32px;
    line-height: 36px;
    letter-spacing: 0.5px;
  }
  .name-plate .person-role {
    font-size: 17px;
    line-height: 20px;
  }
  .accent-bar {
    position: absolute;
    left: 246px;
    top: 188px;
    width: 17px;
    height: 52px;
    background: var(--brand-blue);
  }
  .accent-rule {
    position: absolute;
    left: 268px;
    top: 188px;
    width: 2px;
    height: 82px;
    background: var(--brand-navy);
  }
  .contact-list {
    position: absolute;
    left: 276px;
    top: 197px;
    right: 22px;
    font-family: "Roboto", sans-serif;
    font-size: 18.5px;
    line-height: 23px;
    color: var(--ink-dark);
    white-space: nowrap;
  }
  .contact-list .label { color: var(--brand-blue); }
  .back-band {
    position: absolute;
    left: 0;
    right: 0;
    bottom: 0;
    height: 78px;
    background: radial-gradient(ellipse at 50% 50%, var(--card-black-soft), var(--card-black) 80%);
    display: flex;
    align-items: center;
    justify-content: center;
    font-family: "Didact Gothic", sans-serif;
    font-size: 25px;
    letter-spacing: 0.5px;
    color: var(--text-light);
  }
</style>
</head>
<body>

<section class="card card--front" aria-label="Card front">
  <div class="front-panel">
    <ul class="service-list">
      <li>Custom/New Homes</li>
      <li>Renovations</li>
      <li>Commercial Office/Shop Fit-outs</li>
      <li>Communications &amp; Security Cameras</li>
      <li>Electric Vehicle Chargers</li>
      <li>Airconditioning</li>
    </ul>
  </div>
  <div class="front-brand">
    <span class="brand-mark"></span>
    <span class="brand-name">Vital Spark Electrical</span>
  </div>
</section>

<section class="card card--back" aria-label="Card back">
  <div class="back-brand">
    <span class="brand-mark"></span>
    <span class="brand-name">Vital Spark Electrical</span>
  </div>

  <div class="name-plate">
    <p class="person-name">Tom Harlow</p>
    <p class="person-role">Director/Electrician</p>
  </div>
  <div class="accent-bar"></div>
  <div class="accent-rule"></div>

  <div class="contact-list">
    <p><span class="label">M</span>: 0417 365 208</p>
    <p><span class="label">E</span>:info@vitalsparkelectrical-example.com.au</p>
    <p>R.E.C 57318</p>
  </div>

  <div class="back-band">www.vitalsparkelectrical-example.com.au</div>
</section>

</body>
</html>
```